Brinevale Yacht Management Full Page Ad Flyer

Yacht Management Package also includes the following periodic Monthly services:

Monthly full vessel systems checklist inspections
Diver For Hull Cleaning And Inspection Of Props, Shafts, and Zincs
Interior/Exterior Detailing and scheduled washdowns
Manage Haulout
Pump-out Services
On-call Captain and Crew Services
Updates

Need more time to provide more content to designers and the printing press template file.

Target Market(s)

Vessel owners, motor yachts, sailboats from 25 feet in length up to 125 feet in length. We do not do cruise ships or yachts larger than 125 feet. Someone who has their boat docked at their house or a local marina. We also offer mobile on-site services.

```html
<!DOCTYPE html>
<html lang="en">
<head>
<meta charset="utf-8">
<title>Brinevale Yacht Management – Flyer and Business Card</title>
<link rel="stylesheet" href="https://fonts.googleapis.com/css2?family=Montserrat:wght@400;500;600&display=swap">
<style>
:root{
  --navy:#042d64;
  --sky:#27a3d8;
  --white:#ffffff;
  --bg:#ececec;
  --photo-top:#cfe6f3;
  --photo-mid:#9fbfd6;
  --photo-sea:#2f4661;
}
*{box-sizing:border-box;margin:0;padding:0}
html,body{width:1200px;height:849px;overflow:hidden}
body{background:var(--bg);font-family:"Montserrat",sans-serif;position:relative;color:var(--white)}

.flyer{position:absolute;left:160px;top:67px;width:503px;height:714px;background:var(--white);overflow:hidden}
.flyer-band{position:absolute;left:0;top:319px;width:503px;height:345px;background:var(--navy)}
.flyer-photo{position:absolute;left:31px;top:29px}
.brand{position:absolute;color:var(--navy);font-weight:600;text-align:center;line-height:1}
.flyer .brand{left:276px;top:36px;width:196px}
.brand-name{display:block;font-size:31px;letter-spacing:1px}
.brand-sub{display:block;font-size:10.5px;letter-spacing:2.6px;margin-top:6px}

.service-tag{position:absolute;left:24px;top:334px;width:115px;height:67px;background:var(--sky);border-radius:10px 0 14px 0;padding:10px 0 0 8px;font-size:20.5px;font-weight:500;line-height:1.05;letter-spacing:.5px}
.intro{position:absolute;left:24px;top:408px;width:455px;font-size:10.3px;line-height:1.3;text-align:justify;letter-spacing:.15px}
.rule{position:absolute;left:21px;top:457px;width:464px;height:2px;background:var(--white)}
.package-heading{position:absolute;left:24px;top:468px;font-size:14.8px;font-weight:500;color:var(--sky);line-height:1.32}

.service{position:absolute;display:flex;align-items:center;font-size:10px;line-height:1.3;letter-spacing:.2px}
.service svg{flex:none;width:24px;height:24px;margin-right:8px}
.service svg *{fill:none;stroke:var(--sky);stroke-width:1.6;stroke-linecap:round;stroke-linejoin:round}

.contact{position:absolute;left:0;top:674px;width:503px;text-align:center;color:var(--navy)}
.contact-title{font-size:8.5px;font-weight:600}
.contact-line{margin-top:6px;font-size:7.4px;font-weight:500;display:flex;justify-content:center;gap:8px}
.contact-line span{display:flex;align-items:center;gap:3px}
.contact-line svg{width:9px;height:9px}

.card{position:absolute;left:734px;top:331px;width:306px;height:187px;background:var(--navy);overflow:hidden}
.card-art{position:absolute;left:0;top:0;width:306px;height:116px;background:radial-gradient(ellipse at 70% 40%,#ffffff 0%,#eef3f7 45%,#dde6ee 100%)}
.card-stripe{position:absolute;left:0;top:116px;width:306px;height:2px;background:var(--sky)}
.card-corner{position:absolute;left:0;top:0}
.card .brand{left:174px;top:50px;width:112px}
.card .brand-name{font-size:17px;letter-spacing:.5px}
.card .brand-sub{font-size:6px;letter-spacing:1.3px;margin-top:3px}
.holder{position:absolute;left:22px;top:129px}
.holder-name{font-size:11.2px;font-weight:600}
.holder-line{display:flex;align-items:center;gap:4px;font-size:8.2px;line-height:11.5px}
.holder-line svg{width:8px;height:8px}
</style>
</head>
<body>

<section class="flyer">
  <div class="flyer-band"></div>

  <svg class="flyer-photo" width="442" height="328" viewBox="0 0 442 328" role="img" aria-label="Photo of a white luxury superyacht on calm sea under a clear sky">
    <defs>
      <linearGradient id="photoFill" x1="0" y1="0" x2="0" y2="1">
        <stop offset="0" stop-color="var(--photo-top)"/>
        <stop offset=".55" stop-color="var(--photo-mid)"/>
        <stop offset=".7" stop-color="#b8c4cf"/>
        <stop offset="1" stop-color="var(--photo-sea)"/>
      </linearGradient>
    </defs>
    <path d="M0 0 H245 V10 A55 55 0 0 0 300 64 H442 V328 H210 A210 210 0 0 1 0 118 Z" fill="url(#photoFill)"/>
  </svg>

  <div class="brand"><span class="brand-name">BRINEVALE</span><span class="brand-sub">YACHT MANAGEMENT</span></div>

  <div class="service-tag">OUR<br>SERVICE</div>
  <p class="intro">Brinevale is proud to be a full service provider. Our dedicated Yacht Care service was created specifically to meet the needs of owners who are not able to spend regular time on board their yacht.</p>
  <div class="rule"></div>
  <h2 class="package-heading">Yacht Management Package also includes<br>the following periodic services:</h2>

  <div class="service" style="left:28px;top:518px">
    <svg viewBox="0 0 24 24"><rect x="4" y="4" width="13" height="17" rx="1"/><path d="M8 3h5v3H8zM7 10h7M7 13h7M7 16h4"/><circle cx="18" cy="17" r="3"/></svg>
    <span>Monthly full vessel systems checklist<br>inspections</span>
  </div>
  <div class="service" style="left:28px;top:563px">
    <svg viewBox="0 0 24 24"><path d="M16 3l1.5 4 4 1.5-4 1.5L16 14l-1.5-4-4-1.5 4-1.5zM6 13l1 2.5 2.5 1L7 17.5 6 20l-1-2.5-2.5-1L5 15.5z"/></svg>
    <span>Interior/Exterior Detailing and<br>scheduled washdowns</span>
  </div>
  <div class="service" style="left:28px;top:604px">
    <svg viewBox="0 0 24 24"><circle cx="14" cy="10" r="6"/><circle cx="14" cy="10" r="3.5"/><path d="M9.5 14.5L3 21"/></svg>
    <span>Diver For Hull Cleaning And<br>Inspection Of Props, Shafts,<br>and Zincs</span>
  </div>

  <div class="service" style="left:262px;top:518px">
    <svg viewBox="0 0 24 24"><path d="M3 2v20M3 3h16v3M8 14h12l-2 4H9zM11 14v-3h5v3M2 21h20"/></svg>
    <span style="margin-left:10px">Manage Haulout</span>
  </div>
  <div class="service" style="left:262px;top:562px">
    <svg viewBox="0 0 24 24"><path d="M2 10h20l-2 9H4zM6 10l3-4h6l3 4M8 13v4h3"/></svg>
    <span style="margin-left:10px">Pump-out Services</span>
  </div>
  <div class="service" style="left:262px;top:606px">
    <svg viewBox="0 0 24 24"><path d="M5 4l3 0 1.5 4-2 1.5a10 10 0 0 0 5 5l1.5-2 4 1.5v3a2 2 0 0 1-2 2A15 15 0 0 1 3 6a2 2 0 0 1 2-2z"/><path d="M14 3h7v5h-7z"/></svg>
    <span style="margin-left:10px">On-call Captain and<br>Crew Services</span>
  </div>

  <div class="contact">
    <div class="contact-title">Contact Us at :</div>
    <div class="contact-line">
      <span><svg viewBox="0 0 10 10"><circle cx="5" cy="5" r="4.2" fill="none" stroke="var(--navy)" stroke-width="1"/><path d="M1 5h8M5 1c2 2 2 6 0 8M5 1c-2 2-2 6 0 8" fill="none" stroke="var(--navy)" stroke-width=".7"/></svg>www.brinevaleyachtmanagement.com</span>
      <span><svg viewBox="0 0 10 10"><rect x=".5" y="2" width="9" height="6.5" fill="none" stroke="var(--navy)"/><path d="M.5 2l4.5 4 4.5-4" fill="none" stroke="var(--navy)"/></svg>service@brinevaleyachtmanagement.com</span>
      <span><svg viewBox="0 0 10 10"><path d="M1 4c0-2 8-2 8 0v1H7V4H3v1H1zM2 5.5h6l1 3H1z" fill="var(--navy)"/></svg>(+1) 555-014-2290</span>
    </div>
  </div>
</section>

<section class="card">
  <div class="card-art" role="img" aria-label="Soft white flowing wave texture background"></div>
  <svg class="card-corner" width="32" height="37" viewBox="0 0 32 37">
    <path d="M0 0h12a8 8 0 0 1 8 8v12H0z" fill="var(--sky)"/>
    <path d="M20 20h11v7a3 3 0 0 1-3 3h-8z" fill="var(--sky)"/>
    <path d="M16 30h6v7h-3a3 3 0 0 1-3-3z" fill="var(--sky)"/>
  </svg>
  <div class="card-stripe"></div>
  <div class="brand"><span class="brand-name">BRINEVALE</span><span class="brand-sub">YACHT MANAGEMENT</span></div>
  <div class="holder">
    <div class="holder-name">Rowan Ellis</div>
    <div class="holder-line"><svg viewBox="0 0 10 10"><path d="M1 4c0-2 8-2 8 0v1H7V4H3v1H1zM2 5.5h6l1 3H1z" fill="var(--white)"/></svg>(+1) 555-014-2290</div>
    <div class="holder-line"><svg viewBox="0 0 10 10"><rect x=".5" y="2" width="9" height="6.5" fill="none" stroke="var(--white)"/><path d="M.5 2l4.5 4 4.5-4" fill="none" stroke="var(--white)"/></svg>service@brinevaleyachtmanagement.com</div>
    <div class="holder-line"><svg viewBox="0 0 10 10"><circle cx="5" cy="5" r="4.2" fill="none" stroke="var(--white)"/><path d="M1 5h8M5 1c2 2 2 6 0 8M5 1c-2 2-2 6 0 8" fill="none" stroke="var(--white)" stroke-width=".7"/></svg>www.brinevaleyachtmanagement.com</div>
  </div>
</section>

</body>
</html>
```